QT482 - Shape, Shield, Gauge, Guide - OT Cyber Security Software, KPI Visualisation Software and

Build Website - we require a website with approx 5 tabs on scrolling pane screen - Home, Who We are, Cyber Security, Visualisation, Trusted Partners, Support, Contact, single scrolling panel or tab click to page with images and 2-3 paragraphs of text - wording and links to partners will be provided along with company logo

Target Market(s)

Process Control Markets - Oil and Gas clients, Telecommunications Operators, IOT companies, manufacturing, transport sector etc

Industry/Entity Type

Security

Coding

Coded - Design and coding required

Number of Pages Required

5+ page

Font styles to use
Sans Serif

Colors
0255a3
3176b5
85abd2
f04a50
ec1f27
1b1b1b
474747
919191
d3d3d3

Requirements
Must have
• Scrolling pane / page with tabs along the top -
• Who We are - software and professional services provider for Process Control Cyber Security and Data visualisation
• Shape Shield Gauge Guide -
• define and defend process control networks, measure, manage, visualise data sets from any source etc
• Process Control Cyber Security - images and wording - area for wording can be created and left to be fully populated etc
• Visualisation - data set visualisation from desk top / tablet / mobile device,
• Trusted Partners - links to www.brenvilo.example www.kelmorin.example www.gorvane.example.au
• Support
• Contact Details
• images for cyber security risks etc
• data visualisation / visual KPI - software package
• Support - link to www.gorvane.example.au for NOC and Customer Support - sections for Gold, Silver and Bronze support package - we will add wording later
Nice to have
• Colours - blues / blacks / grey - cyber security information and sections,
• reds etc for visualisation sections
• Use similar colours as logo for rest of pages

```html
<!DOCTYPE html>
<html lang="en">
<head>
<meta charset="utf-8">
<title>QT482 – Shape, Shield, Gauge, Guide</title>
<link href="https://fonts.googleapis.com/css2?family=Open+Sans:wght@400;600;700&family=PT+Sans:wght@400;700&display=swap" rel="stylesheet">
<style>
:root{
  --blue:#0255a3; --blue-mid:#3176b5; --blue-soft:#85abd2;
  --red-soft:#f04a50; --red:#ec1f27;
  --ink:#1b1b1b; --text:#474747; --muted:#919191; --line:#d3d3d3;
  --navy:#2f3b4c; --navy-dark:#263140; --paper:#f3f3f3; --gray:#e4e4e4; --white:#fff;
}
*{box-sizing:border-box;margin:0;padding:0}
html,body{width:1200px;height:4091px;overflow:hidden}
body{font-family:"Open Sans",Arial,sans-serif;color:var(--text);background:var(--white);position:relative}
.section{position:absolute;left:0;width:1200px}
.abs{position:absolute}
h2,h3{font-family:"PT Sans",Arial,sans-serif}

/* header */
.site-header{top:0;height:76px;background:var(--white);z-index:5}
.brand{position:absolute;display:flex;align-items:center;gap:10px;font:700 32px "PT Sans",Arial,sans-serif;color:var(--navy);white-space:nowrap}
.brand i{display:block;width:18px;height:18px;background:var(--red)}
.site-header .brand{left:131px;top:18px}
.call{right:131px;top:10px;font-size:14px;color:var(--ink);display:flex;align-items:center;gap:8px}
.call strong{color:var(--red);font-size:16px}
.nav{left:415px;top:40px;display:flex;gap:6px;font-size:14px;color:var(--ink)}
.nav span{padding:4px 12px}
.nav .active{background:var(--red);color:var(--white)}

.hero{top:76px;height:560px;background:radial-gradient(ellipse at 52% 38%,#7fd0f2 0%,#2a78b4 22%,#153d6a 55%,#0c2544 100%)}

/* who */
.who{top:636px;height:319px;background:var(--navy);color:var(--white);text-align:center}
.who h2{position:absolute;top:50px;width:100%;font-size:22px;font-weight:400}
.who .lead{position:absolute;top:104px;left:0;width:100%;font-weight:700;font-size:14px;line-height:21px}
.who .copy{position:absolute;top:160px;left:360px;width:480px;font-size:13px;line-height:19px;color:#dfe5ee}

/* pillars */
.pillars{top:955px;height:496px;background:var(--paper)}
.pillars .photo{position:absolute;left:0;top:0;width:628px;height:496px;background:linear-gradient(120deg,#4a5566,#2c3646 60%,#3b4656)}
.pillars .words{position:absolute;left:131px;top:170px;color:var(--white);font:700 42px/54px "PT Sans",Arial,sans-serif;letter-spacing:1px}
.cards{position:absolute;left:428px;top:117px;width:641px;height:319px;display:grid;grid-template-columns:1fr 1fr;gap:2px;background:var(--line);box-shadow:0 4px 14px rgba(0,0,0,.15)}
.card{background:var(--white);display:flex;gap:14px;padding:30px 22px}
.card svg{flex:none}
.card h3{font-size:15px;color:var(--ink);margin-bottom:8px}
.card p{font-size:12px;line-height:20px;color:var(--text)}

/* cyber */
.cyber{top:1451px;height:532px;background:var(--white)}
.cyber h2{position:absolute;left:131px;top:80px;font-size:26px;line-height:32px;color:var(--blue-mid);font-weight:400}
.cyber .copy{position:absolute;left:131px;top:170px;width:472px;font-size:13px;line-height:19px}
.cyber .copy p+p{margin-top:18px}
.cyber .photo{position:absolute;left:628px;top:0;width:572px;height:532px;background:radial-gradient(circle at 55% 50%,#5cc6ff 0%,#1a5aa8 30%,#0b2455 65%,#06163a 100%)}

/* visual */
.visual{top:1983px;height:409px;background:var(--red);color:var(--white)}
.visual .devices{position:absolute;left:131px;top:62px;width:464px;height:300px;background:linear-gradient(180deg,#f2f2f2,#cfcfcf);border-radius:6px}
.visual h2{position:absolute;left:641px;top:50px;font-size:34px;font-weight:700;letter-spacing:1px}
.visual .copy{position:absolute;left:641px;top:118px;width:440px;font-size:12px;line-height:19px}
.visual ul{position:absolute;left:641px;top:226px;list-style:none;font-size:12px;line-height:24px}
.visual li{display:flex;align-items:center;gap:10px}
.visual li::before{content:"";width:7px;height:7px;border-radius:50%;background:var(--white)}

/* partners */
.partners{top:2392px;height:294px;background:var(--paper);text-align:center}
.partners h2{position:absolute;top:50px;width:100%;font-size:24px;color:var(--ink)}
.partner{position:absolute;top:2536px;display:flex;align-items:center;gap:12px;font:700 34px "PT Sans",Arial,sans-serif;color:var(--text)}
.partner i{width:30px;height:30px;background:var(--muted);display:block}

/* support */
.support{top:2686px;height:600px;background:var(--gray)}
.support h2{position:absolute;top:44px;width:100%;text-align:center;font-size:24px;color:var(--ink)}
.plan{position:absolute;top:114px;width:300px;height:369px;background:var(--white);box-shadow:0 2px 8px rgba(0,0,0,.08);text-align:center}
.plan header{height:137px;background:var(--navy);color:var(--white);padding-top:18px}
.plan.bronze header{background:var(--red-soft)}
.plan h3{font-size:24px;font-weight:400}
.plan .price{font:700 44px "PT Sans",Arial,sans-serif;margin-top:6px}
.plan .price sup{font-size:22px}
.plan .price small{font-size:13px;font-weight:400}
.plan ul{list-style:none;margin:14px 34px 0;font-size:12px;line-height:30px}
.plan li{border-bottom:1px solid var(--line)}
.plan .btn{display:inline-block;margin-top:14px;background:var(--red);color:var(--white);font-size:12px;font-weight:700;padding:7px 20px}
.noc{position:absolute;left:532px;top:504px;width:136px;height:60px;background:#8a9a28}

/* contact */
.contact{top:3286px;height:526px;background:var(--white)}
.contact h2{position:absolute;top:56px;width:100%;text-align:center;font-size:24px;color:var(--ink)}
.info{position:absolute;left:218px;top:190px;font-size:13px;line-height:20px;color:var(--ink)}
.info h3{font-size:13px;font-weight:700;letter-spacing:.5px;margin-bottom:14px}
.info .row{display:flex;gap:12px;margin-bottom:12px}
.info .row svg{flex:none;margin-top:3px}
.info h3.hours{margin-top:30px;margin-bottom:4px}
.form{position:absolute;left:636px;top:166px;width:362px}
.form .field{height:40px;border:1px solid var(--line);margin-bottom:10px;font-size:12px;color:var(--muted);padding:11px 14px}
.form .field.msg{height:98px}
.form .submit{display:inline-block;margin-top:8px;background:var(--red);color:var(--white);font-size:12px;font-weight:700;padding:9px 26px}

/* footer */
.site-footer{top:3812px;height:279px;background:var(--navy);color:var(--white)}
.site-footer .brand{left:224px;top:104px;color:var(--white)}
.foot{position:absolute;left:445px;font-size:12px}
.foot.label{top:58px;font-weight:700}
.foot.links{top:88px;color:#d6dce5}
.follow{position:absolute;left:445px;top:130px;display:flex;align-items:center;gap:8px;font-size:12px;font-weight:700}
.follow i{width:22px;height:22px;border-radius:50%;background:var(--blue-mid);display:block}
.foot.copy{top:200px;color:#c4ccd8;font-size:11px}
</style>
</head>
<body>

<header class="section site-header">
  <div class="brand"><i></i>QT482</div>
  <div class="abs call">
    <svg width="12" height="16" viewBox="0 0 12 16"><path d="M3 1l2 3-1.5 1.5c.7 2 2 3.6 4 4.8L9 8.8l3 2-1 3c-5 0-10-6-10-12z" fill="#ec1f27"/></svg>
    Call us Now : <strong>555.014.2290</strong>
  </div>
  <nav class="abs nav">
    <span class="active">Home</span><span>Who We are</span><span>Cyber Security</span><span>Visualisation</span><span>Trusted Partners</span><span>Support</span><span>Contact</span>
  </nav>
</header>

<section class="section hero" role="img" aria-label="Photo of a person in a suit touching a glowing unlock icon among hexagon padlock symbols"></section>

<section class="section who">
  <h2>Who We are</h2>
  <p class="lead">Software and professional services provider for Process<br>Control Cyber Security and Data visualisation</p>
  <p class="copy">We protect industrial networks with clear insight into every asset. Our team pairs field experience with modern tools, so operators see risks early and act fast. From refinery to rail, we keep critical systems safe, visible and running with less effort and more confidence.</p>
</section>

<section class="section pillars">
  <div class="photo" role="img" aria-label="Dark photo of a laptop on an office desk"></div>
  <div class="words">SHAPE<br>SHIELD<br>GAUGE<br>GUIDE</div>
  <div class="cards">
    <div class="card">
      <svg width="34" height="44" viewBox="0 0 34 44"><circle cx="17" cy="8" r="6" fill="#474747"/><rect x="9" y="16" width="16" height="26" rx="3" fill="#474747"/></svg>
      <div><h3>SHAPE</h3><p>Baseline your OT communications<br>with passive capture of your assets<br>Know your topology with confidence</p></div>
    </div>
    <div class="card">
      <svg width="34" height="40" viewBox="0 0 34 40"><path d="M17 2l14 5v12c0 10-7 16-14 19C10 35 3 29 3 19V7z" fill="none" stroke="#474747" stroke-width="3"/></svg>
      <div><h3>SHIELD</h3><p>Be alerted to any change in your<br>baseline OT environment in real-time<br>Pro-actively manage your threat</p></div>
    </div>
    <div class="card">
      <svg width="34" height="34" viewBox="0 0 34 34"><path d="M4 26a13 13 0 0 1 26 0" fill="none" stroke="#474747" stroke-width="3"/><path d="M17 26l8-10" stroke="#474747" stroke-width="3"/></svg>
      <div><h3>GAUGE</h3><p>Turn your data sources into powerful<br>Visual Management Tools – trust<br>your data to inform you</p></div>
    </div>
    <div class="card">
      <svg width="34" height="34" viewBox="0 0 34 34"><g stroke="#474747" stroke-width="3"><path d="M3 8h28M3 17h28M3 26h28"/></g><g fill="#474747"><circle cx="10" cy="8" r="4"/><circle cx="23" cy="17" r="4"/><circle cx="14" cy="26" r="4"/></g></svg>
      <div><h3>GUIDE</h3><p>Customise and present your<br>dashboard in minutes<br>Start managing, your way, in minutes</p></div>
    </div>
  </div>
</section>

<section class="section cyber">
  <h2>Process Control<br>Cyber Security</h2>
  <div class="copy">
    <p>Industrial control networks were built for uptime, not for threats. We map every device, watch every link and flag odd traffic the moment it appears. Our passive tools never touch live control loops, so plants keep running while security teams gain full sight of assets, firmware and changes across the site.</p>
    <p>Alerts are ranked by risk, not noise. Operators get plain guidance, engineers get the detail, and managers get a clear picture of exposure. Reports support audits and help plan patching windows without surprise outages or lost production time.</p>
  </div>
  <div class="photo" role="img" aria-label="Illustration of a glowing padlock on a digital globe of hexagon network lines"></div>
</section>

<section class="section visual">
  <div class="devices" role="img" aria-label="Dashboard software shown on a desktop monitor, laptop, tablet and phone"></div>
  <h2>VISUALISATION</h2>
  <p class="copy">See every key figure in one place. Pull data from any source, shape it into clear live dashboards and share it on desktop, tablet or phone. Teams spot trends sooner, decide faster and stay aligned on what matters most.</p>
  <ul>
    <li>Connect historians, databases and live feeds</li>
    <li>Build custom views without writing code</li>
    <li>Share secure dashboards with any team</li>
    <li>Track targets and alerts in real time</li>
  </ul>
</section>

<section class="section partners">
  <h2>Trusted Partners</h2>
</section>
<div class="partner" style="left:250px"><i></i>Brenvilo</div>
<div class="partner" style="left:480px"><i></i>Kelmorin</div>
<div class="partner" style="left:780px"><i></i>Gorvane</div>

<section class="section support">
  <h2>Support</h2>
  <div class="plan" style="left:131px">
    <header><h3>Gold</h3><div class="price">$89,<sup>99</sup><small> / month</small></div></header>
    <ul><li>Remote help desk</li><li>Monthly health check</li><li>Threat feed updates</li><li>Email response 24h</li><li>Quarterly report</li></ul>
    <span class="btn">READ MORE</span>
  </div>
  <div class="plan" style="left:450px">
    <header><h3>Silver</h3><div class="price">$99,<sup>99</sup><small> / month</small></div></header>
    <ul><li>Remote help desk</li><li>Monthly health check</li><li>Threat feed updates</li><li>Email response 24h</li><li>Quarterly report</li></ul>
    <span class="btn">READ MORE</span>
  </div>
  <div class="plan bronze" style="left:769px">
    <header><h3>Bronze</h3><div class="price">$109,<sup>99</sup><small> / month</small></div></header>
    <ul><li>Remote help desk</li><li>Monthly health check</li><li>Threat feed updates</li><li>Email response 24h</li><li>Quarterly report</li></ul>
    <span class="btn">READ MORE</span>
  </div>
  <div class="noc" aria-label="Partner support badge"></div>
</section>

<section class="section contact">
  <h2>Contact us</h2>
  <div class="info">
    <h3>LOCATION</h3>
    <div class="row"><svg width="10" height="14" viewBox="0 0 10 14"><path d="M5 0a5 5 0 0 0-5 5c0 4 5 9 5 9s5-5 5-9a5 5 0 0 0-5-5z" fill="#474747"/><circle cx="5" cy="5" r="2" fill="#fff"/></svg><span>118 Foundry Lane, Harlow Creek,<br>IL 60000</span></div>
    <div class="row"><svg width="10" height="12" viewBox="0 0 12 16"><path d="M3 1l2 3-1.5 1.5c.7 2 2 3.6 4 4.8L9 8.8l3 2-1 3c-5 0-10-6-10-12z" fill="#474747"/></svg><span>555.014.2290</span></div>
    <div class="row"><svg width="12" height="10" viewBox="0 0 12 10"><rect width="12" height="10" fill="#474747"/><path d="M0 0l6 5 6-5" fill="none" stroke="#fff"/></svg><span>info@qt482.example</span></div>
    <h3 class="hours">OPENING HOURS</h3>
    <p>Monday - Saturday : 9.00 am - 10.00 pm</p>
  </div>
  <div class="form">
    <div class="field">Name</div>
    <div class="field">E-mail</div>
    <div class="field">Phone</div>
    <div class="field msg">Message</div>
    <span class="submit">SUBMIT</span>
  </div>
</section>

<footer class="section site-footer">
  <div class="brand"><i></i>QT482</div>
  <div class="foot label">MENU</div>
  <div class="foot links">Home &nbsp;|&nbsp; Who We are &nbsp;|&nbsp; Cyber Security &nbsp;|&nbsp; Visualisation &nbsp;|&nbsp; Trusted Partners &nbsp;|&nbsp; Support &nbsp;|&nbsp; Contact</div>
  <div class="follow">FOLLOW US <i></i><i></i><i></i></div>
  <div class="foot copy">Copyrights @ 2018 All Rights Reserved</div>
</footer>

</body>
</html>
```